High end business card design for custom homebuilding company

Looking for a high end business card design that is unique and elegant. Can use embossing, foil printing, laser die cutting, or any high end printing technique or high end paper. Will upload current design so you can see the logo and what we are using currently, but we want something more unique and elegant. I included our logo to help with design.

Target Market(s)

High end custom home buyers of $1.5 million plus homes. Also real estate developers of high end communities.

Industry/Entity Type

Business

Contact Information for Business Card

Double sided. We want something very elegant and expensive looking. We are looking to incorporate a combination of perhaps linen paper or a high end paper, with foil stamping or embossing/debossing to make the card look unique, but still elegant. We tend to use blacks and golds, but are open to any ideas. Looking for creative and unique design.

Colors

Designer to choose colors to be used in the design.

Requirements
Must have
• High end, elegant look. Can use foil, embossing, or high end papers like linen. We want to make the card unique and interesting, but elegant and expensive looking.
Nice to have
• I am including just some cards I saw that looked interesting for one reason or another. I like a clean elegant design and like both the clean white style, and the blacks. So not sure if we want a black design or white. Would like to see both.

```html
<!DOCTYPE html>
<html lang="en">
<head>
<meta charset="utf-8">
<title>Brightvale Custom Homes – Business Card</title>
<link rel="stylesheet" href="https://fonts.googleapis.com/css2?family=Open+Sans:wght@400;600;700&display=swap">
<style>
  :root {
    --backdrop: #1c1c1d;
    --card-white: #f4f4f2;
    --card-black: #121212;
    --band-dark: #080808;
    --pattern-top: #1e1e1e;
    --pattern-bottom: #141414;
    --gold: #b5a832;
    --ink: #2b2b2b;
    --white: #ffffff;
    --icon-grey: #6b6b6b;
  }
  * { margin: 0; padding: 0; box-sizing: border-box; }
  html, body {
    width: 1200px; height: 1000px; overflow: hidden;
    background: var(--backdrop);
    font-family: "Open Sans", Arial, sans-serif;
  }
  .canvas { position: relative; width: 1200px; height: 1000px; }
  .card {
    position: absolute; left: 220px; width: 760px; height: 434px;
    box-shadow: 0 18px 40px rgba(0,0,0,.55);
    overflow: hidden;
  }
  /* Front */
  .card-front { top: 40px; background: var(--card-white); }
  .brand-front {
    position: absolute; top: 52px; left: 0; right: 0;
    text-align: center;
  }
  .brand-name {
    font-family: "Open Sans", Arial, sans-serif;
    font-weight: 600; color: var(--gold);
    letter-spacing: 3px; text-transform: uppercase;
  }
  .brand-front .brand-name { font-size: 26px; }
  .person-name {
    position: absolute; left: 70px; top: 168px;
    color: var(--gold); font-weight: 700; font-size: 19px;
  }
  .address {
    position: absolute; left: 128px; top: 242px;
    color: var(--ink); font-size: 14px; line-height: 18px;
  }
  .contact-list {
    position: absolute; left: 128px; top: 290px;
    list-style: none; color: var(--ink); font-size: 14px; line-height: 18px;
  }
  .contact-list li { display: flex; align-items: center; gap: 7px; }
  .contact-list li.gap { margin-top: 22px; }
  .contact-list svg { width: 11px; height: 11px; fill: var(--icon-grey); }
  .social {
    position: absolute; right: 50px; top: 160px;
    display: flex; gap: 10px;
  }
  .social span {
    width: 26px; height: 26px; border-radius: 50%;
    background: var(--gold); display: block;
  }
  /* Back */
  .card-back { top: 526px; background: var(--card-black); }
  .pattern-area {
    position: absolute; top: 0; left: 0; right: 0; height: 190px;
    background: linear-gradient(180deg, var(--pattern-top), var(--pattern-bottom));
  }
  .logo-band {
    position: absolute; top: 190px; left: 0; right: 0; height: 130px;
    background: var(--band-dark);
    display: flex; align-items: center; justify-content: center; gap: 14px;
    border-top: 1px solid #2a2a2a; border-bottom: 1px solid #2a2a2a;
  }
  .logo-band .brand-name { font-size: 34px; }
  .brand-dot {
    width: 20px; height: 20px; border-radius: 50%; background: var(--gold);
  }
  .back-web {
    position: absolute; left: 0; right: 0; top: 372px; text-align: center;
    color: var(--white); font-size: 16px; font-weight: 600; letter-spacing: .3px;
  }
  .back-web .accent { color: var(--gold); }
</style>
</head>
<body>
<main class="canvas">
  <section class="card card-front" aria-label="Business card front">
    <div class="brand-front"><span class="brand-name">Brightvale Custom Homes</span></div>
    <p class="person-name">Martin Hale</p>
    <p class="address">Unit 3 14-18 Calder Street,<br>Belmont, WA 6100</p>
    <ul class="contact-list">
      <li><svg viewBox="0 0 12 12"><path d="M2 1h3l1 3-2 1a7 7 0 0 0 3 3l1-2 3 1v3a1 1 0 0 1-1 1A10 10 0 0 1 1 2a1 1 0 0 1 1-1z"/></svg>00 0000 0000</li>
      <li><svg viewBox="0 0 12 12"><path d="M2 1h3l1 3-2 1a7 7 0 0 0 3 3l1-2 3 1v3a1 1 0 0 1-1 1A10 10 0 0 1 1 2a1 1 0 0 1 1-1z"/></svg>00 0000 0000</li>
      <li class="gap"><svg viewBox="0 0 12 12"><path d="M1 2h10v8H1z M1 2l5 4 5-4" stroke="#f4f4f2" stroke-width="1"/></svg>hello@brightvale.com.au</li>
      <li><svg viewBox="0 0 12 12"><circle cx="6" cy="6" r="5"/></svg>www.brightvalecustom.com.au</li>
    </ul>
    <div class="social" aria-label="Social links">
      <span></span><span></span><span></span><span></span><span></span>
    </div>
  </section>

  <section class="card card-back" aria-label="Business card back">
    <div class="pattern-area" role="img" aria-label="Faint repeating brand-mark pattern on black"></div>
    <div class="logo-band">
      <span class="brand-dot"></span>
      <span class="brand-name">Brightvale Custom Homes</span>
    </div>
    <p class="back-web">www.<span class="accent">brightvalehomes</span>.com.au</p>
  </section>
</main>
</body>
</html>
```